Holvery Real Estate Management Consulting

To design a high end company profile that inspires confidence in high net worth individuals and similar clients. The profile to include real estate images, preferably real images. The firm is a Zambian firm and has its target to be comparable to Tesk & Company, Parlowe & Company, Wilder Osten, Lun dorv pelsin wilder osten, TLAV Real estate company as such.

Target Market(s)

Real estate clients such as high net worth individuals, private and public companies, government and international agencies, banks and insurance companies, trusts and pension funds and individual investors. the sub target market group being developers, planners, financiers, market analysts, designers, economists, engineers, architects, construction managers, quantity surveyors and public officials and others

Colors

Designer to choose colors to be used in the design.

Requirements
Must have
• Company logo

```html
<!DOCTYPE html>
<html lang="en">
<head>
<meta charset="utf-8">
<title>Holvery Real Estate – Company Profile Spread</title>
<link href="https://fonts.googleapis.com/css2?family=Montserrat:wght@400;600;700&family=Open+Sans:wght@400;600;700&display=swap" rel="stylesheet">
<style>
:root{
  --navy:#2e3a8c;
  --grey:#8a8d91;
  --dark:#3a3d42;
  --text:#55585d;
  --line:#9a9ca0;
  --orange:#e59a2f;
  --green:#8dbb3c;
  --red:#b8373a;
  --gold:#e0a630;
  --teal:#4f9e86;
  --steel:#4e76ad;
  --page:#ffffff;
  --bg:#e9e9e7;
  --sky:#8fb6de;
}
*{box-sizing:border-box;margin:0;padding:0}
html,body{width:1200px;height:804px;overflow:hidden;background:var(--bg);font-family:"Open Sans",sans-serif;color:var(--text)}
.spread{position:absolute;left:40px;top:12px;width:1120px;height:780px;display:flex;box-shadow:0 6px 24px rgba(0,0,0,.15)}
.page{position:relative;width:560px;height:780px;background:var(--page);overflow:hidden}
.page--left{background:linear-gradient(90deg,#fff 85%,#ececec)}
.page--right{background:linear-gradient(90deg,#ececec,#fff 15%)}

.header{position:absolute;top:26px;left:0;right:0;height:30px}
.header__rule{position:absolute;top:12px;height:1.5px;background:var(--line)}
.header__tab{position:absolute;top:4px;width:48px;height:18px;background:var(--navy)}
.header__arrow{position:absolute;top:3px;width:20px;height:20px;border-radius:50%;background:#fff;border:2px solid var(--navy);color:var(--navy);font-size:10px;font-weight:700;display:flex;align-items:center;justify-content:center}
.logo{position:absolute;top:0;display:flex;align-items:center;gap:5px;font-family:"Open Sans",sans-serif;font-weight:700;font-size:12px;color:var(--navy);letter-spacing:1.5px}
.logo__mark{width:8px;height:8px;background:var(--navy)}

.title{font-family:"Montserrat",sans-serif;font-size:27px;font-weight:700;letter-spacing:.5px;color:var(--navy)}
.title span{color:var(--grey);font-weight:600}
h3{font-family:"Open Sans",sans-serif;font-size:14px;font-weight:600;color:var(--dark);margin-bottom:8px}
p{font-size:8.2px;line-height:1.5;margin-bottom:8px}

.photo{position:absolute;left:330px;top:82px;width:180px;height:180px;background:linear-gradient(160deg,#2c4f86 0%,var(--sky) 45%,#e6eef6 70%,#6f7f92 100%)}

.services{position:absolute;left:56px;top:486px;right:40px;display:flex;gap:24px}
.service{flex:1}
.service__badge{display:flex;align-items:center;height:30px;margin-bottom:14px}
.service__num{width:30px;height:30px;border-radius:8px 0 8px 8px;color:#fff;font-family:"Montserrat",sans-serif;font-weight:700;font-size:15px;display:flex;align-items:center;justify-content:center}
.service__label{background:#eeeeee;height:24px;padding:0 12px;display:flex;align-items:center;font-size:9px;font-weight:700;color:var(--dark);line-height:1.1}
.service ul{padding-left:16px;font-size:8.2px;line-height:1.35}

.footer{position:absolute;bottom:26px;height:38px;display:flex;align-items:center}
.footer__band{background:var(--grey);height:38px;display:flex;align-items:center;color:#fff;font-size:8px;padding:0 40px}
.footer__social{background:var(--navy);height:44px;display:flex;align-items:center;gap:9px;padding:0 26px}
.footer__social i{width:11px;height:11px;background:#fff;border-radius:2px;display:block}
.pagenum{position:absolute;width:18px;height:18px;border-radius:50%;border:2px solid var(--navy);color:var(--navy);font-size:9px;font-weight:700;display:flex;align-items:center;justify-content:center}

.chart{position:absolute;left:40px;top:130px;width:480px;height:300px}
.chart text{font-family:"Open Sans",sans-serif}
</style>
</head>
<body>
<div class="spread">

  <!-- Page 3 -->
  <section class="page page--left">
    <div class="header">
      <div class="header__tab" style="left:0"></div>
      <div class="header__arrow" style="left:34px">›</div>
      <div class="header__rule" style="left:60px;right:150px"></div>
      <div class="logo" style="right:40px"><span class="logo__mark"></span>HOLVERY</div>
    </div>

    <h1 class="title" style="position:absolute;left:56px;top:102px">INSPIRE <span>VALUE</span></h1>

    <div style="position:absolute;left:56px;top:170px;width:250px">
      <h3>WHO WE ARE</h3>
      <p>Holvery | Management Consulting is one of Zambia's leading professional real estate services firms with an outstanding reputation and has its cornerstone the excellence of its people. Since its inception, the business has continued successfully with a national client base, a number of which have retained our services.</p>
    </div>

    <div class="photo" role="img" aria-label="Photograph looking up at glass office towers against a bright cloudy sky"></div>

    <div style="position:absolute;left:56px;top:300px;width:460px">
      <h3>Our Solutions</h3>
      <p>As a preferred property firm we continually monitor property value levels and will provide you with an update on market rents, trends and the position of your property in the marketplace. We continue to roll out our real estate services for you our clients to benefit from the power of our massive experience and database.</p>
      <p>Our system allows you to save on unnecessary research costs and time of doing new research in the marketplace and all due diligence is done when identifying the interests, benefits and rights being researched. We assure our clients and prospective clients that our work is independent, objective and compliant with nationally recognized Laws of the Republic of Zambia.</p>
    </div>

    <h3 style="position:absolute;left:56px;top:452px">Core Services and Scope</h3>

    <div class="services">
      <div class="service">
        <div class="service__badge"><div class="service__num" style="background:var(--navy)">01</div><div class="service__label">Consulting</div></div>
        <ul>
          <li>Advisory Services</li>
          <li>Acquisition, Leasing &amp; Disposal Advise</li>
          <li>Business Plans</li>
          <li>Feasibility studies</li>
          <li>Highest and Best Use Studies</li>
          <li>Market research/analysis</li>
          <li>Planning and development</li>
          <li>Property Condition Assessments</li>
        </ul>
      </div>
      <div class="service">
        <div class="service__badge"><div class="service__num" style="background:var(--orange)">01</div><div class="service__label">Valuations</div></div>
        <ul>
          <li>Agriculture Valuations</li>
          <li>Asset Valuations</li>
          <li>Commercial Valuations</li>
          <li>Leisure/Hotels/Lodges</li>
          <li>Industrial Valuations</li>
          <li>Special purpose Valuations</li>
          <li>Mines Valuations</li>
          <li>Residential Valuations</li>
          <li>Plant, Machinery &amp; Equipment</li>
        </ul>
      </div>
      <div class="service">
        <div class="service__badge"><div class="service__num" style="background:var(--green)">01</div><div class="service__label">Firm's<br>Reference</div></div>
        <ul>
          <li>The Property Valuers Registration Council</li>
          <li>P.O Box 40118</li>
          <li>Lusaka</li>
        </ul>
      </div>
    </div>

    <div class="pagenum" style="right:36px;bottom:76px">3</div>
    <div class="footer" style="left:0;right:0">
      <div class="footer__social" aria-label="Social links"><i></i><i></i><i></i><i></i></div>
      <div class="footer__band" style="flex:1">info@holveryproperty.example | +260 955 018 427/ 0966 204 315</div>
    </div>
  </section>

  <!-- Page 4 -->
  <section class="page page--right">
    <div class="header">
      <div class="logo" style="left:40px"><span class="logo__mark"></span>HOLVERY</div>
      <div class="header__rule" style="left:150px;right:60px"></div>
      <div class="header__arrow" style="right:34px">‹</div>
      <div class="header__tab" style="right:0"></div>
    </div>

    <h1 class="title" style="position:absolute;left:40px;top:80px">SMART <span>MOVE</span></h1>

    <div style="position:absolute;left:40px;top:128px;width:470px">
      <h3 style="margin-bottom:4px">SERVICES AND BUSINESS LINES</h3>
      <p>Holvery Mgt Consulting serves our clients through four main business lines with services for all property types and asset classes.</p>
    </div>

    <svg class="chart" viewBox="0 0 480 300" aria-label="Four business lines">
      <g fill="none" stroke-width="1">
        <polyline points="270,120 270,50 300,50" stroke="var(--gold)"/>
        <polyline points="380,160 380,100 420,100" stroke="var(--teal)"/>
        <polyline points="200,180 200,110 170,110" stroke="var(--red)"/>
        <polyline points="100,220 100,190 60,190" stroke="var(--steel)"/>
      </g>
      <text x="300" y="46" font-size="8" fill="var(--text)">Advisory Services</text>
      <text x="380" y="96" font-size="8" fill="var(--text)">Property Consultancy</text>
      <text x="80" y="100" font-size="8" fill="var(--text)">Urban Planning and</text>
      <text x="80" y="111" font-size="8" fill="var(--text)">Development</text>
      <text x="40" y="186" font-size="8" fill="var(--text)">Valuation Services</text>
      <rect x="240" y="120" width="60" height="60" fill="var(--gold)"/>
      <rect x="350" y="160" width="60" height="60" fill="var(--teal)"/>
      <rect x="170" y="180" width="60" height="60" fill="var(--red)"/>
      <rect x="70" y="220" width="60" height="60" fill="var(--steel)"/>
      <g fill="#fff" font-size="12" font-weight="700" text-anchor="middle">
        <text x="270" y="155">01</text>
        <text x="380" y="195">02</text>
        <text x="100" y="255">03</text>
        <text x="200" y="215">04</text>
      </g>
    </svg>

    <div style="position:absolute;left:40px;top:446px;width:480px">
      <h3>Advisory Services</h3>
      <p>Our advisory services help communities find strategic practical solutions for the most challenging issues facing today's urban, suburban and rural areas.</p>
      <p>We provide expert, independent, timing, candid, and biased input from national real estate, land use, design and planning experts. We help communities gain fresh insight and come to innovative solutions for complex land use and real estate development challenges.</p>
      <p>Our work aims to work with local governments, private developers, community development corporations and many other organizations to address the most challenging real estate and land use issues facing the communities today.</p>
      <p>Holvery Mgt consulting works with industry leaders including developers, planners, financiers, market analysts, designers, economists, engineers, architects, construction managers, quantity surveyors and public officials to provide practical and objective advise that is not available from any other source.</p>
    </div>

    <div class="pagenum" style="left:36px;bottom:76px">4</div>
    <div class="footer" style="left:0;right:0">
      <div class="footer__band" style="flex:1;justify-content:flex-end">info@holveryproperty.example | +260 955 018 427/ 0966 204 315</div>
      <div class="footer__social" aria-label="Social links"><i></i><i></i><i></i><i></i></div>
    </div>
  </section>

</div>
</body>
</html>
```